Kelvaro Store Biz Cards

We are wanting to have one business card for all of the employees to use.

Industry/Entity Type

Business

Requirements
Must have
• ON FRONT Entire Logo on front of card. Black with the letters over. We want to have our website www.kelvarostore.com on front
• ON BACK the address with a simple map . Our address is 2864 West Lumley Ave. Sheridan, Colorado 80247. We want to show address on map as a star. We also want to have a 5% Discount code for biz cards.

```html
<!DOCTYPE html>
<html lang="en">
<head>
<meta charset="utf-8">
<title>Kelvaro Store Business Card</title>
<link href="https://fonts.googleapis.com/css2?family=Nunito:wght@300;400&display=swap" rel="stylesheet">
<style>
  :root {
    --page: #ffffff;
    --card: #000000;
    --accent: #8dc63f;
    --ink-light: #ffffff;
    --map-base: #e6e3dc;
    --map-park: #cfe3c0;
  }
  * { margin: 0; padding: 0; box-sizing: border-box; }
  html, body {
    width: 1200px;
    height: 1197px;
    overflow: hidden;
    background: var(--page);
    font-family: "Nunito", "Helvetica Neue", Arial, sans-serif;
  }
  .canvas { position: relative; width: 1200px; height: 1197px; }
  .card {
    position: absolute;
    background: var(--card);
    width: 755px;
    height: 436px;
  }
  .card--front { left: 84px; top: 192px; }
  .card--back { left: 353px; top: 650px; }

  .brand-name {
    position: absolute;
    left: 0; right: 0;
    top: 165px;
    text-align: center;
    font-weight: 400;
    font-size: 92px;
    line-height: 1;
    letter-spacing: -2px;
    color: var(--ink-light);
  }
  .front-contact {
    position: absolute;
    left: 0; right: 0;
    top: 312px;
    text-align: center;
    color: var(--accent);
    font-weight: 300;
  }
  .front-contact .website { font-size: 27px; line-height: 34px; }
  .front-contact .phone { font-size: 20px; line-height: 30px; }

  .map-area {
    position: absolute;
    left: 57px; top: 66px;
    width: 360px; height: 229px;
    background: linear-gradient(135deg, var(--map-base) 0%, #ece9e2 55%, var(--map-park) 100%);
  }
  .address {
    position: absolute;
    left: 57px; top: 310px;
    color: var(--accent);
    font-weight: 300;
    font-size: 17.5px;
    line-height: 22px;
  }
  .offer {
    position: absolute;
    left: 438px; top: 88px;
    width: 270px;
    text-align: center;
    color: var(--accent);
    font-weight: 300;
  }
  .offer-headline { font-size: 27px; line-height: 36px; }
  .discount-code {
    width: 270px; height: 47px;
    margin-top: 2px;
    background: var(--ink-light);
  }
  .offer-list {
    margin-top: 12px;
    font-size: 18.5px;
    line-height: 25px;
  }
</style>
</head>
<body>
<div class="canvas">
  <section class="card card--front" aria-label="Card front">
    <h1 class="brand-name">Kelvaro Store</h1>
    <div class="front-contact">
      <p class="website">kelvarostore.com</p>
      <p class="phone">call 303.555.0142</p>
    </div>
  </section>

  <section class="card card--back" aria-label="Card back">
    <div class="map-area" role="img" aria-label="Street map of Sheridan, Colorado with a star marking the store location"></div>
    <p class="address">2864 West Lumley Ave. Sheridan,<br>Colorado 80247</p>
    <div class="offer">
      <p class="offer-headline">Show This card<br>for a 5% Discount</p>
      <div class="discount-code" aria-label="Discount code area"></div>
      <p class="offer-list">e cigs, 100s of flavors,<br>supplies, FREE giveaways<br>everyday.</p>
    </div>
  </section>
</div>
</body>
</html>
```